Innovative automotive company needs some flat designs

Hi there. This is your project brief that will tell you everything you need to know. We want to create a Facebook ad that tells a story about the benefits of using our platform. We have a compelling story. We have the words. Now we need the graphics.
Requirements:
Our company's brand identity has the following three elements, futuristic, premium and minimalistic. The design has to be like this too.
Our colour scheme is RGB (255,255,255), 73,225,245, and 5, 7, 9.
Here's our company's landing page. From there you may take a look at our app too.
www.velmorix.io
We have a great story to tell. Help us make it eye-catching. And engaging.
Here are the 4 points/images we want to bring across. Words in brackets should be included in the images.
Words should only take up AT MOST 20% of the space.
THERE SHOULD BE 4 IMAGES (1 FOR EACH POINT). PLEASE DO NOT USE THE ICONS THAT WE HAVE ON OUR WEBSITE. You can refer to the attached for reference. This is the kind of format that we want but the style should be suited to our company brand identity and colour scheme.
Each image should be 600 x 600 pixels
1) Quality Assurance
(3-tier screening to select partner workshops of all expertise. Regular audit and mystery shopping to ensure quality.)
2) Save time and effort
(For each requests, our system chooses the best offers and send them to you. Compare job scope, price, reviews, duration and others at a glance.)
3) No overcharging, no redundant repairs
(Job scope is pre-agreed through the app. Any changes have to be documented.
With these records, our in-house technical expertise and data analytics will identify bad behaviour.)
4) Community Reviews
(Reviews from consumers after each job is completed. Ensure high standards consistently.)

```html
<!DOCTYPE html>
<html lang="en">
<head>
<meta charset="utf-8">
<title>Velmorix – Community Reviews</title>
<link rel="stylesheet" href="https://fonts.googleapis.com/css2?family=Cinzel:wght@400;600&display=swap">
<style>
  :root {
    --paper: #ffffff;
    --ink: #050709;
    --panel-top: #1b2128;
    --panel-mid: #11161b;
    --panel-low: #0b0e12;
    --cyan: #49e1f5;
    --cyan-soft: #6fe3f3;
    --text: #ffffff;
    --logo: #d9dde1;
    --rule: #2f8f97;
  }
  html, body {
    margin: 0;
    padding: 0;
    width: 1200px;
    height: 1200px;
    overflow: hidden;
    background: var(--paper);
  }
  .ad {
    position: relative;
    width: 1200px;
    height: 1200px;
    background: var(--paper);
    font-family: "Cinzel", serif;
  }
  .ad__backdrop {
    position: absolute;
    inset: 0;
    clip-path: polygon(90px 0, 1200px 0, 1200px 1000px, 1096px 1200px, 0 1200px, 0 290px);
    background:
      radial-gradient(ellipse 55% 40% at 78% 62%, rgba(60,72,84,0.35), transparent 70%),
      radial-gradient(ellipse 45% 35% at 30% 35%, rgba(50,60,70,0.30), transparent 70%),
      linear-gradient(180deg, var(--panel-top) 0%, var(--panel-mid) 55%, var(--panel-low) 100%);
  }
  .brand {
    position: absolute;
    top: 108px;
    right: 60px;
    margin: 0;
    font-family: "Cinzel", serif;
    font-weight: 400;
    font-size: 72px;
    letter-spacing: 10px;
    color: var(--logo);
    line-height: 1;
  }
  .ad__rule {
    position: absolute;
    top: 366px;
    left: 150px;
    width: 850px;
    height: 2px;
    background: linear-gradient(90deg, rgba(47,143,151,0.2), var(--rule) 25%, var(--rule) 75%, rgba(47,143,151,0.2));
  }
  .feature {
    position: absolute;
    left: 296px;
    top: 520px;
    width: 720px;
  }
  .feature__title {
    margin: 0 0 18px;
    font-weight: 400;
    font-size: 46px;
    font-variant: small-caps;
    letter-spacing: 3px;
    color: var(--text);
    text-shadow: 0 0 8px rgba(255,255,255,0.55);
    line-height: 1.1;
  }
  .feature__title .initial {
    color: var(--cyan);
    text-shadow: 0 0 8px rgba(73,225,245,0.6);
  }
  .feature__text {
    margin: 0;
    font-size: 30px;
    font-variant: small-caps;
    letter-spacing: 3px;
    line-height: 35px;
    color: var(--text);
  }
  .badge {
    position: absolute;
    left: 86px;
    top: 792px;
    width: 220px;
    height: 172px;
  }
</style>
</head>
<body>
  <main class="ad">
    <div class="ad__backdrop" role="img" aria-label="Dark photograph of a car interior with dashboard and steering wheel"></div>

    <p class="brand">VELMORIX</p>

    <div class="ad__rule"></div>

    <section class="feature">
      <h1 class="feature__title"><span class="initial">C</span>ommunity Reviews</h1>
      <p class="feature__text">Reviews from consumers after<br>each job is completed. Ensure<br>high standards consistently.</p>
    </section>

    <svg class="badge" viewBox="0 0 220 172" aria-hidden="true">
      <rect x="16" y="22" width="190" height="128" rx="8" fill="var(--paper)" transform="rotate(-6 110 86)"/>
      <rect x="18" y="14" width="196" height="132" rx="8" fill="var(--cyan-soft)" transform="rotate(4 110 86)"/>
      <g fill="none" stroke="var(--ink)" stroke-width="4" stroke-linecap="round" stroke-linejoin="round">
        <circle cx="94" cy="56" r="16"/>
        <path d="M72 56 a22 22 0 0 1 44 0"/>
        <path d="M116 60 v8 q0 6 -10 8 h-8"/>
        <path d="M60 140 v-18 q0 -28 34 -28 q34 0 34 28"/>
        <path d="M112 118 h30 l-7 -7"/>
        <path d="M142 132 h-30 l7 7"/>
      </g>
    </svg>
  </main>
</body>
</html>
```